Exciting brochure for new start up in Australia (corporate mentor program)

We are setting up a program called "The Ledger Greenhouse"
The brochure will have the following sections:
Program Framework:
5 Interactive sessions with well-respected CFO (mentor)
- Driving commercial programmes and overcoming barriers
- Executing group strategy and how you can participate
- Leading a transformation
- What does the CFO define as top talent?
- Exploring the career journey to CFO
The program focuses on discussion and insights into the 4 core areas the CFO must master;
1. Strategy & Commercial
2. Operational
3. Decision Making
4. Leadership
(please draw a venn diagram (circles intersecting) using the making one circle representing each other areas noted above. At the intersection (in the middle, please place the term "CFO Success")
Participants
High calibre participants will be hand selected and assessed before joining the program to ensure a "high performance" culture is developed within the program.
As part of the program, participants will be provided with;
- Breakfast and refreshments at each session
- Opportunity to communicate directly with CFO (mentors) in a confidential environment
- Course material and other relevant reading material
- Access to a closed community for networking with other participants (online/ social)
- Access to [kvm]'s "Summit Circle" which offers recruitment services at discounted rates
- Invites to other social, educational and networking opportunities
Please see the www.kvm.com.au website for branding and logo to use on this document.
Updates
Hi all,
The project is reasonably urgent and I'm looking to review designs of the brochure as soon as possible. If you have any questions on this, please let me know.
I'm looking forward to receiving something soon.
Thanks
JT
Target Market(s)
professionals
Font styles to use
Other font styles liked:
- modern font.. corporate yet contemporary
Requirements
Must have
- ven diagram, descriptions provided, professional image, aligned to the [kvm] website
Should not have
- soft colours, missing detail

```html
<!DOCTYPE html>
<html lang="en">
<head>
<meta charset="utf-8">
<title>The Ledger Greenhouse – Brochure</title>
<link href="https://fonts.googleapis.com/css2?family=Roboto:wght@300;400;500;700&display=swap" rel="stylesheet">
<style>
  :root {
    --backdrop: #c6c6c6;
    --navy: #14161d;
    --orange: #e8962a;
    --orange-band: #eaa23a;
    --venn: #eb8f2c;
    --ink: #2b2b2b;
    --ink-soft: #3a3a3a;
    --black-band: #111111;
    --white: #ffffff;
    --light: #e6e6e6;
  }
  * { margin: 0; padding: 0; box-sizing: border-box; }
  html, body { width: 1200px; height: 834px; overflow: hidden; }
  body { background: var(--backdrop); font-family: "Roboto", Arial, sans-serif; position: relative; }

  .page { position: absolute; top: 26px; width: 558px; height: 782px; overflow: hidden; }
  .page--cover { left: 28px; background: var(--navy); color: var(--white); }
  .page--inside { left: 609px; background: var(--white); color: var(--ink); }

  .cover-photo {
    position: absolute; left: 0; top: 0; width: 558px; height: 520px;
    background:
      radial-gradient(ellipse 60% 55% at 48% 30%, #3a4158 0%, rgba(35,40,56,.6) 45%, rgba(20,22,29,0) 80%),
      linear-gradient(180deg, #1c2030 0%, var(--navy) 100%);
  }
  .cover-url { position: absolute; left: 414px; top: 40px; font-size: 11.5px; font-weight: 700; color: var(--orange); }
  .cover-title {
    position: absolute; left: 57px; top: 316px;
    font-size: 52px; font-weight: 700; line-height: 53px; color: var(--orange); letter-spacing: .2px;
  }
  .cover-subtitle {
    position: absolute; left: 114px; top: 442px;
    font-size: 19px; font-weight: 500; line-height: 23px; color: var(--orange);
  }
  .session-list { position: absolute; left: 114px; top: 495px; list-style: none; }
  .session-list li { font-size: 15px; font-weight: 300; line-height: 21px; color: var(--light); padding-left: 14px; position: relative; }
  .session-list li::before { content: "•"; position: absolute; left: 0; font-size: 11px; }

  .brand { position: absolute; left: 112px; top: 676px; display: flex; align-items: center; gap: 12px; }
  .brand-mark { width: 14px; height: 14px; background: var(--orange); }
  .brand-name { font-size: 40px; font-weight: 500; line-height: 44px; letter-spacing: .5px; }
  .page--cover .brand-name { color: var(--white); }
  .page--inside .brand-name { color: var(--ink); }
  .contact { position: absolute; left: 285px; top: 662px; font-size: 12px; font-weight: 700; line-height: 15.5px; }
  .contact p + p { margin-top: 7px; }
  .page--cover .contact { color: var(--white); }
  .page--inside .contact { color: var(--ink); }

  .venn { position: absolute; left: 0; top: 0; }
  .venn-label { font-family: "Roboto", Arial, sans-serif; font-size: 12.5px; font-weight: 400; fill: var(--ink-soft); }
  .venn-core-label { font-family: "Roboto", Arial, sans-serif; font-size: 13px; font-weight: 700; fill: var(--ink); }

  .focus { position: absolute; left: 285px; top: 68px; font-size: 15px; font-weight: 300; line-height: 21px; color: var(--ink); }
  .focus ol { list-style: none; margin-top: 6px; }

  .band-participants { position: absolute; left: 0; top: 272px; width: 558px; height: 118px; background: var(--black-band); color: var(--light); }
  .band-participants h2 { position: absolute; left: 71px; top: 17px; font-size: 18.5px; font-weight: 400; color: var(--white); }
  .band-participants p { position: absolute; left: 71px; top: 44px; width: 405px; font-size: 14.5px; font-weight: 300; line-height: 18.5px; }

  .band-benefits { position: absolute; left: 0; top: 390px; width: 558px; height: 251px; background: var(--orange-band); }
  .band-benefits h2 { position: absolute; left: 59px; top: 20px; font-size: 18.5px; font-weight: 500; line-height: 21px; color: var(--ink); }
  .benefit-list { position: absolute; left: 59px; top: 70px; width: 445px; list-style: none; }
  .benefit-list li { font-size: 14.5px; font-weight: 300; line-height: 20px; color: var(--ink-soft); padding-left: 13px; position: relative; }
  .benefit-list li::before { content: "•"; position: absolute; left: 0; font-size: 10px; }
  .benefit-list .narrow { width: 395px; }
</style>
</head>
<body>

<section class="page page--cover">
  <div class="cover-photo" role="img" aria-label="Photograph of a businessman in a dark suit and tie with arms crossed, against a dark background"></div>
  <p class="cover-url">www.kvm.com.au</p>
  <h1 class="cover-title">THE LEDGER<br>GREENHOUSE</h1>
  <p class="cover-subtitle">5 interactive sessions with<br>well-respected CFOs</p>
  <ul class="session-list">
    <li>Driving commercial programmes and overcoming barriers</li>
    <li>Executing group strategy and how you can participate</li>
    <li>Leading a transformation</li>
    <li>How does the CFO define as top talent?</li>
    <li>Exploring the career journey to CFO</li>
  </ul>
  <div class="brand"><span class="brand-mark"></span><p class="brand-name">KVM</p></div>
  <div class="contact">
    <p>Level 7, 118 Harbourline Street<br>Sydney NSW, Australia 2000</p>
    <p>Phone: +61 2 9000 4100<br>Fax: +61 2 9000 4133<br>Email: info@kvm.com.au</p>
  </div>
</section>

<section class="page page--inside">
  <svg class="venn" width="270" height="272" viewBox="0 0 270 272" role="img" aria-label="Venn diagram of four core areas overlapping at CFO Success">
    <g fill="var(--venn)" fill-opacity="0.62">
      <circle cx="149" cy="104" r="75"/>
      <circle cx="110" cy="146" r="75"/>
      <circle cx="188" cy="146" r="75"/>
      <circle cx="149" cy="186" r="75"/>
    </g>
    <text class="venn-label" x="149" y="53" text-anchor="middle">Strategy &amp;</text>
    <text class="venn-label" x="149" y="65" text-anchor="middle">Commercial</text>
    <text class="venn-label" x="149" y="238" text-anchor="middle">Operational</text>
    <text class="venn-label" transform="translate(65 146) rotate(-90)" text-anchor="middle">Leadership</text>
    <text class="venn-label" transform="translate(236 146) rotate(90)" text-anchor="middle">Decision</text>
    <text class="venn-label" transform="translate(223 146) rotate(90)" text-anchor="middle">Making</text>
    <text class="venn-core-label" x="149" y="141" text-anchor="middle">CFO</text>
    <text class="venn-core-label" x="149" y="154" text-anchor="middle">Success</text>
  </svg>

  <div class="focus">
    <p>The program focuses on discussion<br>and insights into the 4 core areas<br>the CFO must master;</p>
    <ol>
      <li>1. Strategy &amp; Commercial</li>
      <li>2. Operational</li>
      <li>3. Decision Making</li>
      <li>4. Leadership</li>
    </ol>
  </div>

  <div class="band-participants">
    <h2>Participants</h2>
    <p>High calibre participants will be hand selected and assessed before joining the program to ensure a "high performance" culture is developed within the program.</p>
  </div>

  <div class="band-benefits">
    <h2>As part of the program,<br>participants will be provided with;</h2>
    <ul class="benefit-list">
      <li>Breakfast and refreshments at each session</li>
      <li>Opportunity to communicate directly with CFO (mentors) in a confidential environment</li>
      <li>Course material and other relevant reading material</li>
      <li class="narrow">Access to a closed community for networking with other participants (online/ social)</li>
      <li>Access to [kvm]'s "Summit Circle"</li>
      <li>Invites to other social, educational and networking opportunities</li>
    </ul>
  </div>

  <div class="brand"><span class="brand-mark"></span><p class="brand-name">KVM</p></div>
  <div class="contact">
    <p>Level 7, 118 Harbourline Street<br>Sydney NSW, Australia 2000</p>
    <p>Phone: +61 2 9000 4100<br>Fax: +61 2 9000 4133<br>Email: info@kvm.com.au</p>
  </div>
</section>

</body>
</html>
```